Promo flyer

Simple, clean flyer to hand to customers during a wedding expo. These will be handed out to foot traffic.
Flyer must be easy to read, simple but pretty and in line with our branding.
Logo must be shown
Images and or styling tools
Please look at our website to get a feel for the brand/colours/etc.
www.larkspurlocks.co.uk
The images attached are samples from the website....something along these lines. Images can be used alone and wording separate.
HD images of the girls alone can be provided so its best quality for print.

Mention
-Shop our luxurious hair extensions & styling tools
-www.larkspurlocks.co.uk
-QT50 = 50% off all styling tools
-Complimentary colour match for hair extensions. Email uk@larkspurlocks.com.

Requirements
Must have
• Logo must be shown
• Images and or styling tools
• BEFORE & AFTER Images (1 before and after) - refer to this link below.
• https://www.larkspurlocks.com/pages/before-afters-see-the-difference
• Please look at our website to get a feel for the brand/colours/etc.
• www.larkspurlocks.co.uk
• The images attached are samples from the website....something along these lines. Images can be used alone and wording separate.
Nice to have
• Water colour behind the discount codes so this stands out

```html
<!DOCTYPE html>
<html lang="en">
<head>
<meta charset="utf-8">
<title>Larkspur Locks – Promo Flyer</title>
<link rel="stylesheet" href="https://fonts.googleapis.com/css2?family=Marcellus&family=Montserrat:wght@300;400;500&display=swap">
<style>
  :root {
    --backdrop: #e9e6e3;
    --paper: #ffffff;
    --brand-pink: #e0468a;
    --brand-pink-deep: #d93f82;
    --ink: #1d1d1f;
    --ink-soft: #333336;
    --white: #ffffff;
  }
  * { box-sizing: border-box; margin: 0; padding: 0; }
  html, body {
    width: 1027px; height: 1200px; overflow: hidden;
    background: var(--backdrop);
  }
  .flyer {
    position: absolute; left: 167px; top: 103px;
    width: 693px; height: 992px;
    background: var(--paper);
    font-family: "Montserrat", Arial, sans-serif;
    color: var(--ink);
    overflow: hidden;
  }
  .site-url {
    position: absolute; right: 70px; top: 70px;
    font-size: 15px; font-weight: 500; letter-spacing: 0.2px;
  }
  .brand-mark {
    position: absolute; left: 462px; top: 146px; width: 142px;
    text-align: center;
  }
  .brand-mark__circle {
    width: 116px; height: 116px; margin: 0 auto;
    border: 2px solid var(--brand-pink); border-radius: 50%;
  }
  .brand-mark__name {
    margin-top: 14px;
    font-size: 13px; letter-spacing: 3px; font-weight: 400;
    color: var(--brand-pink); white-space: nowrap;
  }
  .hero-band {
    position: absolute; left: 0; top: 340px; width: 100%; height: 260px;
    background: linear-gradient(180deg, var(--brand-pink) 0%, var(--brand-pink-deep) 100%);
  }
  .hero-photo {
    position: absolute; left: 38px; top: 32px; width: 395px; height: 568px;
    background: linear-gradient(180deg, #e8d3c4 0%, #6b4638 35%, #efe9e4 60%, #d8b7a4 75%, #1b1b1b 90%);
    border-radius: 180px 180px 0 0;
    opacity: 0.9;
  }
  .tagline-your {
    position: absolute; left: 433px; top: 410px;
    width: 150px; height: 46px;
    transform-origin: 0 0; transform: translate(0, 150px) rotate(-90deg);
    font-family: "Marcellus", Georgia, serif;
    font-size: 44px; line-height: 46px; color: var(--ink); letter-spacing: 1px;
  }
  .tagline-words {
    position: absolute; left: 491px; top: 400px;
    font-family: "Marcellus", Georgia, serif;
    font-size: 42px; line-height: 57px; color: var(--white);
  }
  .shop-heading {
    position: absolute; left: 50px; top: 638px;
    font-size: 21.5px; font-weight: 400; line-height: 35px;
    letter-spacing: 0.3px; color: var(--ink);
  }
  .tool-list {
    position: absolute; left: 48px; top: 730px;
    display: flex; gap: 12px; list-style: none;
  }
  .tool-list__item {
    width: 111px; height: 111px; border-radius: 50%;
    border: 3px solid var(--brand-pink);
    background: radial-gradient(circle, #3a3a3a 0%, #8a8a8a 35%, #ffffff 60%);
  }
  .promo-code {
    position: absolute; left: 50px; top: 876px;
    width: 358px; height: 35px;
    background: var(--brand-pink);
    border-radius: 0 18px 18px 0;
    padding-left: 10px;
    font-family: "Marcellus", Georgia, serif;
    font-size: 21px; line-height: 35px; color: var(--white);
  }
  .footer-note {
    position: absolute; left: 50px; top: 947px;
    font-size: 14.5px; color: var(--ink-soft);
  }
  .footer-email {
    position: absolute; left: 460px; top: 947px;
    font-size: 14.5px; color: var(--ink-soft);
  }
  .footer-email__label { color: var(--brand-pink); }
  .before-after {
    position: absolute; left: 484px; top: 615px; width: 160px; height: 305px;
  }
  .before-after__photo {
    position: absolute; left: 28px; width: 104px; height: 136px;
    border-radius: 50px 50px 4px 4px;
    background: linear-gradient(180deg, #2a1e1a 0%, #3b2a24 55%, #c59a80 80%, #111 100%);
  }
  .before-after__photo--before { top: 6px; }
  .before-after__photo--after { top: 155px; }
  .before-after__tag {
    position: absolute; height: 9px; padding: 0 6px;
    background: var(--brand-pink); color: var(--white);
    font-size: 5.5px; letter-spacing: 1px; line-height: 9px;
  }
  .before-after__tag--before { left: 4px; top: 22px; }
  .before-after__tag--after { left: 109px; top: 174px; }
  .before-after__rules { position: absolute; left: 0; top: 0; }
</style>
</head>
<body>
  <main class="flyer">
    <div class="hero-band"></div>
    <div class="hero-photo" role="img" aria-label="Model with long dark wavy hair holding a curling wand, wearing a white crop top"></div>

    <p class="site-url">www.larkspurlocks.co.uk</p>

    <div class="brand-mark">
      <div class="brand-mark__circle"></div>
      <p class="brand-mark__name">LARKSPUR LOCKS</p>
    </div>

    <div class="tagline-your">YOUR</div>
    <p class="tagline-words">Look<br>Style<br>Passion</p>

    <h2 class="shop-heading">SHOP OUR LUXURIOUS HAIR<br>EXTENSIONS &amp; STYLING TOOLS</h2>

    <ul class="tool-list">
      <li class="tool-list__item" role="img" aria-label="Interchangeable curling wand set"></li>
      <li class="tool-list__item" role="img" aria-label="Slim hair straightener"></li>
      <li class="tool-list__item" role="img" aria-label="Black and gold flat iron"></li>
    </ul>

    <p class="promo-code">QT50 = 50% off all styling tools</p>

    <p class="footer-note">Complimentary colour match for hair extensions.</p>
    <p class="footer-email"><span class="footer-email__label">Email</span> uk@larkspurlocks.com</p>

    <section class="before-after">
      <div class="before-after__photo before-after__photo--before" role="img" aria-label="Back view of dark hair before extensions"></div>
      <div class="before-after__photo before-after__photo--after" role="img" aria-label="Back view of long wavy dark hair after extensions"></div>
      <span class="before-after__tag before-after__tag--before">BEFORE</span>
      <span class="before-after__tag before-after__tag--after">AFTER</span>
      <svg class="before-after__rules" width="160" height="305" viewBox="0 0 160 305">
        <line x1="0" y1="144" x2="159" y2="129" stroke="#e0468a" stroke-width="2.5"/>
        <line x1="0" y1="297" x2="159" y2="282" stroke="#e0468a" stroke-width="2.5"/>
      </svg>
    </section>
  </main>
</body>
</html>
```